Web Design Project for NCYB

Hi,
I am looking for a website design for the Northern Council for Youth Boards.
This is an organisation which helps with legal disputes and other challenges which involve children.  The company want a web page which is professional but friendly.  The purpose of the website is to explain what the organisation does and to give people a place where they can download documents and information.
The homepage will have a video on the page.  ALSO, we would prefer the site to have a left hand navigation (not a top navigation).
I have enclosed the logo, a picture of the old (rubbish) home page and a screenshot from the video (you are welcome to change the dimensions).
If you have any questions, please ask.
-K
UPDATE: 6th DECEMBER:
Thanks for the designs so far.  I promise to give feedback to every single person.  In the meantime, can I just say that there's some good designs so far but I don't think anyone has nailed this yet.
So, I am uploading a screenshot called "theylikethis.jpg".  This is a screenshot from a website that the client says they like.
Can I also say, it's okay to reduce the size of the video.  I'm seeing a lot of massive videos.
Thanks folks!
UPDATE:  You can view a live demo of the site that they like at www.demohostqz.co.uk
UPDATE:  I've just found another good example of a site with a left nav at www.brightresourcehubnet.com

Hi,
Hi folks,
Had a quick look at the designs and just to say how impressed I am with the qualityand choice. There are a few that caught my eye and I'll try and narrow them down.I've also passed the link onto the other representatives for their input beforemaking a final choice. If I don't hear from any of the other represenatatives by Wednesday, I'll chose adesign and let you know. Once again many thanks for the quick response in gettingdesigns done and really looking forward to seeing the completed website.
Industry/Entity Type
Legal
Requirements
Must have
- a video player (any size of your choosing)
a left side navigation
the logo

```html
<!DOCTYPE html>
<html lang="en">
<head>
<meta charset="utf-8">
<title>Northern Council for Youth Boards</title>
<link href="https://fonts.googleapis.com/css2?family=Lato:wght@300;400;700&family=Oswald:wght@500&display=swap" rel="stylesheet">
<style>
:root{
  --bg-deep:#1d4aa6;
  --bg-light:#5a85cc;
  --brand:#0a3a95;
  --brand-bright:#1556c4;
  --ink:#111;
  --nav-ink:#1a4ba8;
  --rule:#1a4ba8;
  --muted:#555;
  --white:#fff;
  --pdf:#d4161c;
}
*{box-sizing:border-box;margin:0;padding:0}
html,body{width:1170px;height:1200px;overflow:hidden}
body{
  font-family:'Lato',sans-serif;
  background:radial-gradient(ellipse at 50% 95%,var(--bg-light) 0%,var(--bg-deep) 70%);
  position:relative;
}
.page{position:absolute;left:166px;top:0;width:838px;height:1078px;background:var(--white);box-shadow:0 0 8px rgba(0,0,0,.25)}
.abs{position:absolute}
/* header */
.site-header{left:20px;top:0;width:798px;height:154px;background:var(--brand);overflow:hidden}
.header-photo{position:absolute;right:0;top:0;width:400px;height:154px;
  background:linear-gradient(90deg,var(--brand) 0%,rgba(190,150,130,.55) 35%,#c9a48c 60%,#d9b9a6 100%)}
.brand-mark{position:absolute;left:36px;top:62px;display:flex;align-items:center;gap:6px;color:var(--white);font-size:17px;font-weight:400}
.brand-mark .dot{width:10px;height:10px;border-radius:50%;background:var(--white)}
.site-title{position:absolute;left:115px;top:44px;color:var(--white);font-weight:700;font-size:34px;line-height:32px;letter-spacing:-.3px}
/* nav */
.side-nav{left:19px;top:172px;width:132px;list-style:none}
.side-nav li{height:30.8px;border-bottom:1.5px solid var(--rule);display:flex;align-items:center;justify-content:center;font-size:13px;color:var(--nav-ink);font-weight:400}
.side-nav li.active{background:var(--brand);color:var(--white);font-weight:700;border-top:1.5px solid var(--rule);height:29px;margin-bottom:1.5px}
/* video */
.video{left:170px;top:172px;width:464px;height:262px;box-shadow:0 14px 14px -10px rgba(0,0,0,.35)}
.video-frame{position:absolute;inset:0 0 28px 0;background:radial-gradient(circle at 45% 40%,#d9a070 0%,#b96b3c 30%,#6a8a2e 65%,#3f6b1a 100%)}
.video-tools{position:absolute;right:6px;top:6px;display:flex;flex-direction:column;gap:4px}
.video-tools span{width:20px;height:16px;background:#111;border-radius:2px;display:block}
.video-bar{position:absolute;left:0;right:0;bottom:0;height:28px;background:#0b0b0b;display:flex;align-items:center;padding:0 6px;gap:8px;color:var(--white);font-size:8px}
.play{width:28px;height:18px;background:#222;display:flex;align-items:center;justify-content:center}
.track{flex:1;height:6px;border:1px solid #666;border-radius:3px;position:relative}
.track .time{position:absolute;top:-10px;left:0;background:#fff;color:#000;font-size:6px;padding:0 2px}
.hd{color:#3a8cff;font-weight:700;font-style:normal}
/* content */
.content{left:170px;width:464px;color:var(--ink)}
.content h1,.content h2{font-weight:400;font-size:20px;letter-spacing:-.2px}
.content p{font-size:11.2px;line-height:14.4px;font-weight:300;color:#000;margin-top:14px}
.content p:first-of-type{margin-top:16px}
/* sidebar */
.sidebar{left:654px;width:164px}
.panel-head{height:28px;background:var(--brand);color:var(--white);font-weight:700;font-size:13px;display:flex;align-items:center;justify-content:center}
.blog-list{list-style:none;margin-top:16px}
.blog-list li{display:flex;gap:6px;height:38px;margin-bottom:16px;align-items:center}
.blog-thumb{width:38px;height:38px;border:1px solid #bbb;background:linear-gradient(135deg,#e8d3c5,#b98d74 60%,#7a8b99)}
.blog-title{font-size:11.5px;color:#000}
.blog-sub{font-size:8px;color:#333}
.promo{background:radial-gradient(circle at 50% 40%,var(--brand-bright),var(--brand) 80%);color:var(--white);text-align:center;height:140px}
.promo .big{font-weight:700;font-size:26px;line-height:30px;padding-top:10px}
.promo .mid{font-weight:300;font-size:21px;line-height:23px}
.promo .cta{font-weight:700;font-size:15px;margin-top:22px}
.promo .sub{font-weight:300;font-size:13px;line-height:16px;margin-top:2px}
.pdf-icon{margin:8px auto 0;display:block}
.social{background:var(--brand);height:184px;padding:10px 6px;color:var(--white)}
.social-row{display:flex;gap:6px;margin-bottom:14px}
.social-square{width:30px;height:30px;border-radius:4px;background:#dfe8f6;flex:none}
.social-name{font-family:'Oswald',sans-serif;font-size:16px;line-height:18px}
.social-text{font-size:9.5px;line-height:12px;margin-top:3px}
.social-actions{display:flex;gap:10px;margin-top:5px;align-items:center}
.btn-small{background:#e9edf4;color:#3b5b9a;font-size:9px;padding:2px 5px;border:1px solid #c5cfe0;border-radius:2px}
.count{background:var(--white);color:#000;font-size:11px;padding:2px 8px;border-radius:2px}
.count.strong{color:var(--brand);font-weight:700;font-size:13px;padding:2px 12px}
/* footer */
.footer-rule{left:0;top:1024px;width:838px;height:1px;background:#aaa}
.copyright{left:32px;top:1034px;font-size:10.5px;color:#000}
.footer-nav{left:362px;top:1036px;display:flex;gap:14px;list-style:none;font-size:9.5px;color:#000}
</style>
</head>
<body>
<div class="page">
  <header class="site-header abs">
    <div class="header-photo" role="img" aria-label="Photo of a teacher helping two children reading"></div>
    <div class="brand-mark"><span class="dot"></span>NCYB</div>
    <div class="site-title">Northern Council<br>for Youth Boards</div>
  </header>

  <ul class="side-nav abs">
    <li class="active">HOME</li>
    <li>ABOUT US</li>
    <li>NEWS</li>
    <li>CONFERENCES</li>
    <li>MINTES</li>
    <li>ANNUAL REPORT</li>
    <li>ARCHIVE</li>
    <li>CONTACT US</li>
    <li>LINKS</li>
  </ul>

  <div class="video abs">
    <div class="video-frame" role="img" aria-label="Video still of a child holding alphabet blocks spelling LEARN"></div>
    <div class="video-tools"><span></span><span></span><span></span></div>
    <div class="video-bar">
      <div class="play"><svg width="8" height="9"><path d="M0 0L8 4.5L0 9Z" fill="#fff"/></svg></div>
      <div class="track"><span class="time">00:00</span></div>
      <em class="hd">HD</em>
    </div>
  </div>

  <section class="content abs" style="top:459px">
    <h1>Welcome to&nbsp; NCYB...</h1>
    <p>Lorem Ipsum is simply dummy text of the printing and typesetting industry. Lorem Ipsum has been the industry's standard dummy text ever since the 1500s, when an unknown printer took a galley of type and scrambled it to make a type specimen book. It has survived not only five centuries, but also the leap into electronic typesetting, remaining essentially unchanged. It was popularised in the 1960s with the release of Typeplate sheets containing Lorem Ipsum passages, and more recently with desktop publishing software like Pagecraft Studio including versions of Lorem Ipsum.</p>
    <p>Lorem Ipsum is simply dummy text of the printing and typesetting industry. Lorem Ipsum has been the industry's standard dummy text ever since the 1500s, when an unknown printer took a galley of type and scrambled it to make a type specimen book. It has survived not only five centuries, but also the leap into electronic typesetting, remaining essentially unchanged.</p>
    <p>Lorem Ipsum has been the industry's standard dummy text ever since the 1500s, when an unknown printer took a galley of type and scrambled it to make a type specimen book. It has survived not only five centuries.</p>
  </section>

  <section class="content abs" style="top:750px">
    <h2>Why Was The NCYB FORMED?</h2>
    <p>Lorem Ipsum is simply dummy text of the printing and typesetting industry. Lorem Ipsum has been the industry's standard dummy text ever since the 1500s, when an unknown printer took a galley of type and scrambled it to make a type specimen book. It has survived not only five centuries, but also the leap into electronic typesetting, remaining essentially unchanged.</p>
  </section>

  <section class="content abs" style="top:870px">
    <h2>Objectives</h2>
    <p>Lorem Ipsum has been the industry's standard dummy text ever since the 1500s, when an unknown printer took a galley of type and scrambled it to make a type specimen book.</p>
  </section>

  <aside class="sidebar abs" style="top:171px">
    <div class="panel-head">FROM THE BLOG</div>
    <ul class="blog-list">
      <li><div class="blog-thumb" role="img" aria-label="Portrait photo"></div><div><div class="blog-title">Lorem Ipsum is simply</div><div class="blog-sub">Lorem Ipsum is simply</div></div></li>
      <li><div class="blog-thumb" role="img" aria-label="Photo of children"></div><div><div class="blog-title">Lorem Ipsum is simply</div><div class="blog-sub">Lorem Ipsum is simply</div></div></li>
      <li><div class="blog-thumb" role="img" aria-label="Portrait photo"></div><div><div class="blog-title">Lorem Ipsum is simply</div><div class="blog-sub">Lorem Ipsum is simply</div></div></li>
      <li><div class="blog-thumb" role="img" aria-label="Portrait photo"></div><div><div class="blog-title">Lorem Ipsum is simply</div><div class="blog-sub">Lorem Ipsum is simply</div></div></li>
    </ul>
  </aside>

  <div class="sidebar abs promo" style="top:463px">
    <div class="big">Need Help?</div>
    <div class="mid">Ask us legal<br>Question.</div>
    <div class="cta">Click to Email</div>
  </div>

  <div class="sidebar abs promo" style="top:622px">
    <div class="big">Download</div>
    <div class="sub">Legal Documents<br>and information</div>
    <svg class="pdf-icon" width="38" height="50" viewBox="0 0 38 50">
      <path d="M2 0H28L38 10V50H2Z" fill="var(--pdf)"/>
      <path d="M28 0V10H38Z" fill="#f5a3a5"/>
      <text x="20" y="45" font-family="Lato,sans-serif" font-size="8" font-weight="700" fill="#fff" text-anchor="middle">PDF</text>
    </svg>
  </div>

  <div class="sidebar abs social" style="top:781px">
    <div class="social-row">
      <div class="social-square"></div>
      <div>
        <div class="social-name">We're on Friendloop</div>
        <div class="social-text">Like us to see our daily<br>updates!</div>
        <div class="social-actions"><span class="btn-small">Like</span><span class="count">20</span></div>
      </div>
    </div>
    <div class="social-row">
      <div class="social-square"></div>
      <div>
        <div class="social-name">We're on Chirpline</div>
        <div class="social-text">Like us to see our daily<br>updates!</div>
        <div class="social-actions"><span class="btn-small">Post</span><span class="count strong">241</span></div>
      </div>
    </div>
  </div>

  <div class="footer-rule abs"></div>
  <div class="copyright abs">Copyright © 2012&nbsp; The NCYB</div>
  <ul class="footer-nav abs">
    <li>Home</li><li>About Us</li><li>News</li><li>Conferences</li><li>Mintes</li><li>Annual Report</li><li>Archive</li><li>Contact Us</li><li>Links</li>
  </ul>
</div>
</body>
</html>
```